Pet product line, needs a label design

We are a pharmaceutical company focused on animal health. We have been in the Mexican and Central American market for 10 years. During this time we have developed our line for production animals (beef, poultry, dairy, pigs...) and now we want to develop a line for pets.
Our first product are some pills made of Yucca (Yucca schidigera) which helps the digestive system of cats and dogs improve, reducing gas production and diminishing the bad smell of the pet feces.
We are looking for a design that can represent our new product line using this new product as an example, its name is 'VENTORAN'. The brand umbrella is BQ Vita, I am attaching this logo.
We need an attractive and original design with a strong personality, capable of jumping to the eyes of the consumer (pet owner) and also attractive for the Veterinarian who will recommend the product.
We want to highlight the benefits of the product by developing icons to the three main claims of the product.
We hope you will find this project attractive and challenging!!

Target Market(s)

Pet owners (mainly dog and cat)

Veterinarians

Industry/Entity Type

Pharmaceutical

Requirements
Must have
• * Product name (VENTORAN)
* Label Information (added in a word document)
* Band umbrella logo BQ Vita
* GREAT DESIGN
* The design should be horizontal (5cm height and 13 cm width)
Nice to have
• Nice product name design

Icon designs for the following claims (in spanish):
+ Limpia el trato digestivo (Cleans the digestive tract)
+ Reduce los malos olores (Reduces odors)
+ Propicia la digestión completa (Promotes complete digestion)

```html
<!DOCTYPE html>
<html lang="es">
<head>
<meta charset="utf-8">
<title>VENTORAN · BQ Vita</title>
<link rel="stylesheet" href="https://fonts.googleapis.com/css2?family=Kaushan+Script&family=PT+Sans:wght@400;700&display=swap">
<style>
  :root{
    --brand-blue:#0b9fc6;
    --pale-blue:#bfe6f1;
    --navy:#2b3f8f;
    --teal-text:#1ba6c9;
    --ink:#333333;
    --paper:#ffffff;
    --rule:#555555;
  }
  *{box-sizing:border-box;margin:0;padding:0}
  html,body{width:1135px;height:1200px;overflow:hidden;background:var(--paper)}
  body{position:relative;font-family:"PT Sans",sans-serif;color:var(--ink)}

  /* main horizontal label */
  .label{position:absolute;left:5px;top:20px;width:908px;height:375px;overflow:hidden;background:var(--brand-blue)}
  .label svg{position:absolute;inset:0}
  .label-art{position:absolute;left:40px;top:40px;width:320px;height:250px;border-radius:40% 60% 50% 50%;background:radial-gradient(circle at 50% 55%,var(--paper) 45%,var(--pale-blue) 85%)}
  .label-feather{position:absolute;left:494px;top:21px;width:130px;height:60px;border-radius:60px 6px;background:linear-gradient(120deg,var(--paper),var(--pale-blue));opacity:.85}
  .label-bubbles{position:absolute;left:600px;top:215px;width:300px;height:110px;border-radius:50%;background:radial-gradient(ellipse,rgba(255,255,255,.55),rgba(255,255,255,0) 70%)}
  .label-title{position:absolute;left:430px;top:78px;font-family:"Kaushan Script",cursive;font-size:96px;font-weight:400;color:var(--paper);letter-spacing:1px;line-height:1.2}
  .brand{position:absolute;display:flex;align-items:center;gap:10px;color:var(--navy);font-family:"PT Sans",sans-serif;font-weight:700}
  .label .brand{left:690px;top:300px;font-size:52px}
  .brand .brand-square{display:inline-block;background:var(--navy)}
  .label .brand .brand-square{width:30px;height:30px}

  /* sachet panels */
  .sachet{position:absolute;top:830px;width:196px;height:357px}
  .sachet > svg{position:absolute;inset:0}
  .sachet-1{left:20px}.sachet-2{left:245px}.sachet-3{left:472px}.sachet-4{left:702px}
  .sachet .band{position:absolute;left:0;top:193px;width:196px;height:76px}
  .sachet .band svg{width:100%;height:100%}
  .sachet-title{position:absolute;font-family:"Kaushan Script",cursive;font-weight:400;color:var(--teal-text)}
  .sachet-front .sachet-title{left:26px;top:65px;font-size:34px}
  .sachet-front .art{position:absolute;left:60px;top:30px;width:80px;height:40px;border-radius:40px 4px;background:linear-gradient(90deg,var(--pale-blue),var(--teal-text))}
  .sachet .brand{font-size:22px;gap:6px}
  .sachet .brand .brand-square{width:13px;height:13px}
  .sachet-front .brand{left:52px;top:308px}

  .copy{position:absolute;font-size:7.5px;line-height:1.35}
  .copy h4{font-weight:700;font-size:7.5px}
  .copy ul{list-style:none}
  .copy li::before{content:"";display:inline-block;width:5px;height:5px;margin-right:4px;background:var(--teal-text);border-radius:50%}
  .ingredients{left:14px;top:40px;width:170px;color:var(--teal-text)}
  .ingredients p{margin-top:10px}
  .band-title{position:absolute;left:84px;top:200px;font-family:"Kaushan Script",cursive;font-size:22px;color:var(--paper)}
  .band-brand{position:absolute;left:128px;top:226px;font-size:11px;font-weight:700;color:var(--navy)}
  .maker{left:20px;top:284px;width:165px;font-size:8px}

  .analysis{left:16px;top:32px;width:168px}
  .analysis table{width:100%;border-collapse:collapse;margin-top:8px}
  .analysis td{font-size:7.5px;padding:1px 0;border-bottom:1px solid var(--teal-text)}
  .analysis .contents{margin-top:16px}
  .dosage{left:16px;top:282px;width:170px}
  .dosage p + p{margin-top:8px}
</style>
</head>
<body>

<section class="label" aria-label="Etiqueta principal VENTORAN">
  <svg width="908" height="375" viewBox="0 0 908 375" aria-hidden="true">
    <circle cx="200" cy="200" r="205" fill="var(--paper)"/>
    <path d="M480 375 C510 320 570 340 610 310 C650 275 700 290 740 260 C790 230 860 245 908 225 L908 375 Z" fill="var(--paper)"/>
  </svg>
  <div class="label-art" role="img" aria-label="Silueta ilustrada de la cabeza de un gato dibujada con trazo azul"></div>
  <div class="label-feather" role="img" aria-label="Pluma ilustrada en blanco"></div>
  <div class="label-bubbles" role="img" aria-label="Grupo de burbujas blancas"></div>
  <h1 class="label-title">Ventoran</h1>
  <div class="brand"><span class="brand-square"></span>BQ Vita</div>
</section>

<!-- back panel -->
<section class="sachet sachet-1" aria-label="Sobre, reverso">
  <svg viewBox="0 0 196 357" aria-hidden="true"><path d="M10 1 H186 L195 18 V356 H1 V18 Z" fill="none" stroke="var(--rule)"/><path d="M1 18 H195" stroke="var(--rule)"/></svg>
  <div class="copy ingredients">
    <h4>Ingredientes Activos</h4>
    <ul><li>Saponinas</li><li>Glicocomponentes</li></ul>
    <p><strong>Efectos benéficos en mascotas</strong><br>Reduce significativamente los malos olores en los desechos de las mascotas</p>
    <ul><li>Reduce el estrés</li><li>Limpia el tracto digestivo</li><li>Propicia una digestión completa</li><li>Efectos anti-inflamatorios</li><li>Efectos antimicrobianos</li></ul>
  </div>
  <div class="band"><svg viewBox="0 0 196 76" preserveAspectRatio="none" aria-hidden="true"><rect x="1" width="194" height="76" fill="var(--brand-blue)"/><path d="M1 76 V30 C20 0 60 10 70 40 C80 60 60 76 60 76 Z" fill="var(--paper)"/></svg></div>
  <span class="band-title">Ventoran</span>
  <span class="band-brand">BQ Vita</span>
  <div class="copy maker">Elaborado para :<br>Quintara Internacional, S.A. de C.V.<br>Av. Los Laureles 2450<br>Jardines del Sol CP 44300<br>Guadalajara, Jal.</div>
</section>

<!-- front panel -->
<section class="sachet sachet-2 sachet-front" aria-label="Sobre, frente">
  <svg viewBox="0 0 196 357" aria-hidden="true"><path d="M10 1 H186 L195 18 V356 H1 V18 Z" fill="none" stroke="var(--rule)"/><path d="M1 18 H195" stroke="var(--rule)"/></svg>
  <div class="art" role="img" aria-label="Pluma ilustrada en azul"></div>
  <h2 class="sachet-title">Ventoran</h2>
  <div class="band"><svg viewBox="0 0 196 76" preserveAspectRatio="none" aria-hidden="true"><rect x="1" width="194" height="76" fill="var(--brand-blue)"/><path d="M1 76 V20 C30 -5 90 5 110 40 C125 65 110 76 110 76 Z" fill="var(--paper)"/></svg></div>
  <div class="brand"><span class="brand-square"></span>BQ Vita</div>
</section>

<!-- information panel -->
<section class="sachet sachet-3" aria-label="Sobre, información">
  <svg viewBox="0 0 196 357" aria-hidden="true"><path d="M10 1 H186 L195 18 V356 H1 V18 Z" fill="none" stroke="var(--rule)"/><path d="M1 18 H195" stroke="var(--rule)"/></svg>
  <div class="copy analysis">
    <h4>Análisis bromatológico</h4>
    <table>
      <tr><td>Humedad Max.&nbsp; 8.2 %</td></tr>
      <tr><td>Proteína Cruda Max.&nbsp; 2.0 %</td></tr>
      <tr><td>Grasa Cruda Max.&nbsp; 0.5 %</td></tr>
      <tr><td>Fibra Cruda Max. 30.0 %</td></tr>
      <tr><td>Cenizas Max. 11.0 %</td></tr>
      <tr><td>Carbohidratos Max. 42.5 %</td></tr>
      <tr><td>Excipiente c.b.p.</td></tr>
    </table>
    <p class="contents">Contenido<br>Yucca schidigera extracto pulverizado</p>
  </div>
  <div class="band"><svg viewBox="0 0 196 76" preserveAspectRatio="none" aria-hidden="true"><rect x="1" width="194" height="76" fill="var(--brand-blue)"/><path d="M100 76 C120 50 150 45 170 30 C180 20 190 25 195 20 V76 Z" fill="var(--paper)"/></svg></div>
  <div class="copy dosage">
    <p>Contenido<br>60 tabletas</p>
    <p>Dosis<br>Mascotas pequeñas : 1 tableta al día<br>Mascotas grandes : 2 tabletas al día</p>
  </div>
</section>

<!-- front panel, repeat -->
<section class="sachet sachet-4 sachet-front" aria-label="Sobre, frente">
  <svg viewBox="0 0 196 357" aria-hidden="true"><path d="M10 1 H186 L195 18 V356 H1 V18 Z" fill="none" stroke="var(--rule)"/><path d="M1 18 H195" stroke="var(--rule)"/></svg>
  <div class="art" role="img" aria-label="Pluma ilustrada en azul"></div>
  <h2 class="sachet-title">Ventoran</h2>
  <div class="band"><svg viewBox="0 0 196 76" preserveAspectRatio="none" aria-hidden="true"><rect x="1" width="194" height="76" fill="var(--brand-blue)"/><path d="M1 76 V20 C30 -5 90 5 110 40 C125 65 110 76 110 76 Z" fill="var(--paper)"/></svg></div>
  <div class="brand"><span class="brand-square"></span>BQ Vita</div>
</section>

</body>
</html>
```